HIgh-end jewelry designer needs a business card design

I need a business card design for the ecclectic & rather expensive jewelry designs. My approach to my work is to combine very old jewelry offset with contemporary items. I enjoy the idea of legacy as well as repurposing finely crafted items that are not possible to create any longer. My desire is to celebrate the past in a contemporary & funky way. The name of my business is VELLORINE. I see my business card design as simple & yet enigmatic as possible. In the end... clean, simple & understated is the look I am after. Thank you for your consideration...

Target Market(s)

I will use this business card for the trade as well as customers

Industry/Entity Type

Business

Contact Information for Business Card

Marta Quorrin Owner/Designer 555-203-7718

Requirements
Must have
• Clean & simple sophisticated design using the word "Vellorinne" as the logo. I like the idea of a play on the word itself, perhaps even using different fonts (i.e.: a bold helvetica combined with a lovely script). I'm afraid to say more because I don't want to limit creative input. Gosh, sometimes it's ok to break the rules!
Nice to have
• In my mind, I have imagined this business card to be simple, using my company name "Vellorine" in a playful yet sophisticated manner. I believe that doing something beautifully simple can be a true challenge. I have imagined something with just black & white, however I am open to ideas... after all that's why I'm here!
Should not have
• As Mozart once said... "It has too many notes!" I know I'm being silly, but I don't want it to be complicated or overly ornate.

```html
<!DOCTYPE html>
<html lang="en">
<head>
<meta charset="utf-8">
<title>Vellorine — Business Card</title>
<link rel="stylesheet" href="https://fonts.googleapis.com/css2?family=Jost:wght@300&family=Roboto:wght@300&display=swap">
<style>
  :root {
    --canvas-bg: #f7f7f7;
    --card-front: #ffffff;
    --card-edge: #dcdcdc;
    --card-back: #4d2e47;
    --logo-ink: #6e4f67;
    --contact-ink: #9a7f94;
  }
  html, body {
    margin: 0;
    padding: 0;
    overflow: hidden;
  }
  body {
    width: 1200px;
    height: 900px;
    background: var(--canvas-bg);
    position: relative;
  }
  .card {
    position: absolute;
    left: 343px;
    width: 510px;
    height: 284px;
    border-radius: 43px;
    box-sizing: border-box;
  }
  .card-front {
    top: 137px;
    background: var(--card-front);
    border: 1px solid var(--card-edge);
    display: flex;
    align-items: center;
    justify-content: center;
  }
  .brand-name {
    margin: 0;
    font-family: "Jost", sans-serif;
    font-weight: 300;
    font-size: 36px;
    letter-spacing: 0.32em;
    margin-right: -0.32em;
    color: var(--logo-ink);
    line-height: 1;
    transform: translateY(-4px);
  }
  .card-back {
    top: 439px;
    margin-top: 0;
    top: 438px;
    background: var(--card-back);
  }
  .contact-line {
    position: absolute;
    left: 0;
    right: 0;
    bottom: 28px;
    margin: 0;
    text-align: center;
    font-family: "Roboto", sans-serif;
    font-weight: 300;
    font-size: 15.5px;
    letter-spacing: 0.02em;
    color: var(--contact-ink);
  }
</style>
</head>
<body>
  <section class="card card-front" aria-label="Card front">
    <h1 class="brand-name">VELLORINE</h1>
  </section>
  <section class="card card-back" aria-label="Card back">
    <p class="contact-line">Marta Quorrin Owner/Designer 555-203-7718</p>
  </section>
</body>
</html>
```